Fun and Splashy Flyer Design

We need a flyer designed for our new car cleaning brand! We have looked around, and the stock options either look way too dark/serious/exclusive, or they look too shiny/stock image.

We need something that can be more subtle, that works with our work van.

For this project we would like a photoshop file with individual layers, and you can just put placeholder text for the main slogan, a header 1, header 2, bullet point and body text.

What we're really looking for are the transitions between images and elements, font colours and pairings and design accents.

We want the brand to be fun, clean, happy and straightforward (slightly minimalist). Please message if you have any questions!

```html
<!DOCTYPE html>
<html lang="en">
<head>
<meta charset="utf-8">
<title>Sudsy Lane Car Care – Mobile Car Cleaning Flyer</title>
<link rel="stylesheet" href="https://fonts.googleapis.com/css2?family=Poppins:wght@700;800;900&family=Open+Sans:wght@400;600;700&family=Lato:wght@400;700&display=swap">
<style>
  :root {
    --sky: #1ba6e8;
    --sky-deep: #1487c9;
    --water-top: #3aa9df;
    --water-mid: #62c1ec;
    --water-low: #a5def6;
    --sun: #ffdd00;
    --ink: #2a2a2a;
    --paper: #ffffff;
    --frost: #eaf8ff;
  }
  * { margin: 0; padding: 0; box-sizing: border-box; }
  html, body { width: 846px; height: 1200px; overflow: hidden; background: var(--paper); }
  .flyer {
    position: relative; width: 846px; height: 1200px; overflow: hidden;
    background: var(--paper); font-family: "Open Sans", sans-serif; color: var(--ink);
  }
  .abs { position: absolute; }
  .hero-bg { left: 0; top: 0; }

  .brand-badge { left: 40px; top: 38px; width: 168px; height: 168px; border-radius: 50%;
    background: var(--sun); display: flex; align-items: center; justify-content: center; text-align: center; }
  .brand-badge span { font-family: "Poppins", sans-serif; font-weight: 800; font-size: 22px; line-height: 1.15; color: var(--sky-deep); }

  .headline { font-family: "Poppins", sans-serif; font-weight: 900; color: var(--frost);
    text-shadow: 0 3px 6px rgba(0, 70, 120, .35); white-space: nowrap; line-height: 1;
    transform-origin: left top; }
  .headline-1 { left: 230px; top: 28px; font-size: 90px; letter-spacing: 1px; transform: scaleY(1.17); }
  .headline-2 { left: 324px; top: 123px; font-size: 74px; letter-spacing: 0; transform: scaleY(1.23); }

  .slogan { left: 232px; width: 570px; text-align: center; color: var(--paper); white-space: nowrap; line-height: 1; }
  .slogan-main { top: 218px; font-family: "Poppins", sans-serif; font-size: 24px; font-weight: 800; letter-spacing: 1px; }
  .slogan-sub { top: 254px; font-family: "Open Sans", sans-serif; font-size: 16.5px; font-weight: 700; letter-spacing: 2px; }

  .team-photo { left: 26px; top: 292px; }

  .about-kicker { left: 25px; top: 570px; font-family: "Poppins", sans-serif; font-weight: 900; font-size: 31px; line-height: 1; color: var(--ink); }
  .about-title { left: 23px; top: 593px; font-family: "Poppins", sans-serif; font-weight: 900; font-size: 51px; line-height: 1; color: var(--sky); }
  .about-body { left: 23px; top: 643px; width: 362px; font-size: 16.8px; line-height: 20.5px; letter-spacing: .4px; }

  .support-icon { left: 409px; top: 568px; }
  .support-title { left: 486px; top: 566px; font-family: "Poppins", sans-serif; font-weight: 900; font-size: 26px; color: var(--sky); letter-spacing: 1px; line-height: 1.2; }
  .support-phone { left: 483px; top: 592px; font-family: "Poppins", sans-serif; font-weight: 800; font-size: 33px; line-height: 1.2; color: var(--ink); }
  .support-body { left: 494px; top: 636px; width: 300px; font-family: "Lato", sans-serif; font-size: 15.6px; line-height: 18.5px; }

  .gallery { left: 403px; top: 693px; }

  .service { left: 23px; width: 350px; }
  .service-tick { position: absolute; left: 0; top: 0; }
  .service-title { position: absolute; left: 45px; top: -1px; font-family: "Poppins", sans-serif; font-weight: 900; font-size: 21px; line-height: 1.3; color: var(--sky); letter-spacing: .5px; white-space: nowrap; }
  .service-text { position: absolute; left: 46px; top: 32px; font-family: "Lato", sans-serif; font-size: 15.6px; line-height: 18.5px; width: 310px; }
  .service-1 { top: 755px; }
  .service-2 { top: 840px; }
  .service-3 { top: 934px; }

  .extras-title { left: 405px; top: 886px; font-family: "Poppins", sans-serif; font-weight: 900; font-size: 28.5px; line-height: 1.3; color: var(--sky); letter-spacing: .5px; white-space: nowrap; }
  .extras-list { left: 405px; top: 932px; list-style: none; }
  .extras-list li { display: flex; align-items: center; height: 32px; font-family: "Open Sans", sans-serif; font-weight: 700; font-size: 18.5px; white-space: nowrap; }
  .extras-list svg { margin-right: 16px; flex: none; }

  .footer-band { left: 190px; top: 1125px; width: 656px; height: 75px; background: var(--sun); }
  .footer-house { left: 22px; top: 1054px; }
  .footer-brand { left: 53px; top: 1087px; width: 108px; height: 108px; border-radius: 50%;
    background: #bfe6fa; display: flex; align-items: center; justify-content: center; text-align: center; }
  .footer-brand span { font-family: "Poppins", sans-serif; font-weight: 800; font-size: 15px; line-height: 1.15; color: var(--sky-deep); }
  .contact-title { left: 228px; top: 1090px; font-family: "Poppins", sans-serif; font-weight: 900; font-size: 24px; line-height: 1.3; color: var(--sky); letter-spacing: 1px; }
  .contact-icon-pin { left: 228px; top: 1133px; }
  .contact-icon-mail { left: 456px; top: 1133px; }
  .contact-text { top: 1138px; font-family: "Open Sans", sans-serif; font-weight: 600; font-size: 15px; line-height: 19px; color: var(--ink); }
  .contact-address { left: 286px; }
  .contact-web { left: 515px; }
</style>
</head>
<body>
<main class="flyer">

  <svg class="abs hero-bg" width="846" height="540" viewBox="0 0 846 540" aria-hidden="true">
    <defs>
      <linearGradient id="water" x1="0" y1="0" x2="0" y2="1">
        <stop offset="0" stop-color="var(--water-top)"/>
        <stop offset=".55" stop-color="var(--water-mid)"/>
        <stop offset="1" stop-color="var(--water-low)"/>
      </linearGradient>
      <radialGradient id="waterGlowA" cx=".5" cy=".5" r=".5">
        <stop offset="0" stop-color="#ffffff" stop-opacity=".35"/>
        <stop offset="1" stop-color="#ffffff" stop-opacity="0"/>
      </radialGradient>
      <radialGradient id="waterShadeB" cx=".5" cy=".5" r=".5">
        <stop offset="0" stop-color="#1580c0" stop-opacity=".35"/>
        <stop offset="1" stop-color="#1580c0" stop-opacity="0"/>
      </radialGradient>
      <clipPath id="waterClip">
        <path d="M0 0H846V345C760 400 640 440 530 450C350 460 150 380 0 350Z"/>
      </clipPath>
    </defs>
    <g clip-path="url(#waterClip)">
      <rect width="846" height="460" fill="url(#water)"/>
      <ellipse cx="120" cy="60" rx="260" ry="120" fill="url(#waterShadeB)"/>
      <ellipse cx="720" cy="90" rx="240" ry="140" fill="url(#waterShadeB)"/>
      <ellipse cx="520" cy="170" rx="300" ry="110" fill="url(#waterGlowA)"/>
      <ellipse cx="160" cy="280" rx="240" ry="90" fill="url(#waterGlowA)"/>
      <ellipse cx="700" cy="330" rx="200" ry="90" fill="url(#waterGlowA)"/>
    </g>
    <path d="M0 350C150 380 350 460 530 450C640 440 760 400 846 345V440C760 470 640 490 530 495C350 500 150 410 0 380Z" fill="var(--sun)"/>
    <path d="M0 380C150 410 350 500 530 495C640 490 760 470 846 440V480C760 510 640 522 530 522C350 522 150 450 0 432Z" fill="var(--sky-deep)"/>
  </svg>

  <div class="abs brand-badge"><span>Sudsy Lane<br>Car Care</span></div>

  <h1>
    <span class="abs headline headline-1">MOBILE CAR</span>
    <span class="abs headline headline-2">CLEANING</span>
  </h1>
  <p class="abs slogan slogan-main">DUMMY TEXT DUMMY TEXT DUMMY</p>
  <p class="abs slogan slogan-sub">DUMMY TEXT DUMMY TEXT DUMMY TEXT</p>

  <svg class="abs team-photo" width="514" height="272" viewBox="0 0 514 272" role="img" aria-label="Photo of two team members in yellow shirts standing beside the branded white and yellow cleaning van">
    <defs>
      <linearGradient id="vanTone" x1="0" y1="0" x2="0" y2="1">
        <stop offset="0" stop-color="#f6f9fc"/>
        <stop offset=".6" stop-color="#e6edf2"/>
        <stop offset=".78" stop-color="#f5dc55"/>
        <stop offset="1" stop-color="#d4dadf"/>
      </linearGradient>
      <filter id="frameShadow" x="-5%" y="-5%" width="110%" height="115%">
        <feDropShadow dx="0" dy="4" stdDeviation="5" flood-color="#0b4f7a" flood-opacity=".25"/>
      </filter>
    </defs>
    <rect x="6" y="4" width="502" height="258" rx="16" fill="url(#vanTone)" stroke="var(--paper)" stroke-width="5" filter="url(#frameShadow)"/>
  </svg>

  <p class="abs about-kicker">ABOUT OUR</p>
  <h2 class="abs about-title">COMPANY</h2>
  <p class="abs about-body">Lorem ipsum dolor sit amet, consectetur adipiscing elit, sed do eiusmod tempor incididunt ut labore et dolore magna aliqua. consectetur adipiscing elit, sed</p>

  <svg class="abs support-icon" width="58" height="66" viewBox="0 0 58 66" aria-hidden="true">
    <polygon points="29,0 58,16.5 58,49.5 29,66 0,49.5 0,16.5" fill="var(--sky)"/>
    <path d="M21 20c2-1.5 4-1 5 1l2 4c.6 1.3.2 2.6-.8 3.4l-1.6 1.2c1 2.8 3 5 5.8 6.3l1.3-1.5c.9-1 2.3-1.3 3.5-.6l3.8 2.2c1.8 1 2.1 3.2.6 4.8l-1.6 1.6c-2 2-6 1.5-10-1.3C24 38 19.5 32 18.6 26.6 18.2 23.7 19 21.3 21 20Z" fill="var(--paper)"/>
  </svg>
  <h3 class="abs support-title">CALL SUPPORT</h3>
  <p class="abs support-phone">+123 4567 8900</p>
  <p class="abs support-body">Lorem ipsum dolor sit amet, consectetur adipiscing elit, sed do eiusmod tempor</p>

  <svg class="abs gallery" width="425" height="160" viewBox="0 0 425 160">
    <defs>
      <linearGradient id="galleryFoam" x1="0" y1="0" x2="1" y2="1">
        <stop offset="0" stop-color="#3a3d42"/><stop offset="1" stop-color="#c9ced3"/>
      </linearGradient>
      <linearGradient id="galleryDash" x1="0" y1="0" x2="1" y2="1">
        <stop offset="0" stop-color="#2d2f33"/><stop offset="1" stop-color="#8e8a86"/>
      </linearGradient>
      <linearGradient id="galleryWheel" x1="0" y1="0" x2="1" y2="0">
        <stop offset="0" stop-color="#c8323a"/><stop offset=".5" stop-color="#3b3d40"/><stop offset="1" stop-color="#d8353c"/>
      </linearGradient>
    </defs>
    <g role="img" aria-label="Photo of a gloved hand washing a foamy car headlight">
      <polygon points="67.5,2 133,40 133,118 67.5,156 2,118 2,40" fill="var(--paper)" stroke="var(--sky)" stroke-width="5"/>
      <polygon points="67.5,10 125,44 125,114 67.5,148 10,114 10,44" fill="url(#galleryFoam)"/>
    </g>
    <g role="img" aria-label="Photo of a cloth wiping a car dashboard">
      <polygon points="210.5,2 276,40 276,118 210.5,156 145,118 145,40" fill="var(--paper)" stroke="var(--sky)" stroke-width="5"/>
      <polygon points="210.5,10 268,44 268,114 210.5,148 153,114 153,44" fill="url(#galleryDash)"/>
    </g>
    <g role="img" aria-label="Photo of a soapy wheel on a red car">
      <polygon points="355,2 420.5,40 420.5,118 355,156 289.5,118 289.5,40" fill="var(--paper)" stroke="var(--sky)" stroke-width="5"/>
      <polygon points="355,10 412.5,44 412.5,114 355,148 297.5,114 297.5,44" fill="url(#galleryWheel)"/>
    </g>
  </svg>

  <section class="abs service service-1">
    <svg class="service-tick" width="28" height="28" viewBox="0 0 28 28" aria-hidden="true"><circle cx="14" cy="14" r="11.5" fill="none" stroke="var(--sun)" stroke-width="3.5"/><path d="M8.5 14.5l3.8 3.6 7.2-7.4" fill="none" stroke="var(--sun)" stroke-width="3.2" stroke-linecap="round" stroke-linejoin="round"/></svg>
    <h3 class="service-title">OUR BEST SERVICES</h3>
    <p class="service-text">Lorem ipsum dolor sit amet, consectetur adipiscing elit, sed do eiusmod tempor</p>
  </section>
  <section class="abs service service-2">
    <svg class="service-tick" width="28" height="28" viewBox="0 0 28 28" aria-hidden="true"><circle cx="14" cy="14" r="11.5" fill="none" stroke="var(--sun)" stroke-width="3.5"/><path d="M8.5 14.5l3.8 3.6 7.2-7.4" fill="none" stroke="var(--sun)" stroke-width="3.2" stroke-linecap="round" stroke-linejoin="round"/></svg>
    <h3 class="service-title">OUR OTHER SERVICES</h3>
    <p class="service-text">Lorem ipsum dolor sit amet, consectetur adipiscing elit, sed do eiusmod tempor</p>
  </section>
  <section class="abs service service-3">
    <svg class="service-tick" width="28" height="28" viewBox="0 0 28 28" aria-hidden="true"><circle cx="14" cy="14" r="11.5" fill="none" stroke="var(--sun)" stroke-width="3.5"/><path d="M8.5 14.5l3.8 3.6 7.2-7.4" fill="none" stroke="var(--sun)" stroke-width="3.2" stroke-linecap="round" stroke-linejoin="round"/></svg>
    <h3 class="service-title">OUR GOOD SERVICES</h3>
    <p class="service-text">Lorem ipsum dolor sit amet, consectetur adipiscing elit, sed do eiusmod tempor</p>
  </section>

  <h3 class="abs extras-title">OUR OTHER SERVICES</h3>
  <ul class="abs extras-list">
    <li><svg width="20" height="20" viewBox="0 0 20 20" aria-hidden="true"><circle cx="10" cy="10" r="8.3" fill="none" stroke="var(--sky)" stroke-width="2.4"/><path d="M6 10.3l2.7 2.6 5.2-5.3" fill="none" stroke="var(--sky)" stroke-width="2.3" stroke-linecap="round" stroke-linejoin="round"/></svg>Lorem ipsum dolor sit amet</li>
    <li><svg width="20" height="20" viewBox="0 0 20 20" aria-hidden="true"><circle cx="10" cy="10" r="8.3" fill="none" stroke="var(--sky)" stroke-width="2.4"/><path d="M6 10.3l2.7 2.6 5.2-5.3" fill="none" stroke="var(--sky)" stroke-width="2.3" stroke-linecap="round" stroke-linejoin="round"/></svg>consectur adipiscing elit</li>
    <li><svg width="20" height="20" viewBox="0 0 20 20" aria-hidden="true"><circle cx="10" cy="10" r="8.3" fill="none" stroke="var(--sky)" stroke-width="2.4"/><path d="M6 10.3l2.7 2.6 5.2-5.3" fill="none" stroke="var(--sky)" stroke-width="2.3" stroke-linecap="round" stroke-linejoin="round"/></svg>sed do eiusmod tempor</li>
    <li><svg width="20" height="20" viewBox="0 0 20 20" aria-hidden="true"><circle cx="10" cy="10" r="8.3" fill="none" stroke="var(--sky)" stroke-width="2.4"/><path d="M6 10.3l2.7 2.6 5.2-5.3" fill="none" stroke="var(--sky)" stroke-width="2.3" stroke-linecap="round" stroke-linejoin="round"/></svg>incididunt ut labore et</li>
  </ul>

  <div class="abs footer-band"></div>
  <svg class="abs footer-house" width="169" height="146" viewBox="0 0 169 146" aria-hidden="true">
    <polygon points="84.5,0 169,32 169,146 0,146 0,32" fill="var(--sky-deep)"/>
  </svg>
  <div class="abs footer-brand"><span>Sudsy Lane<br>Car Care</span></div>

  <h3 class="abs contact-title">CONTACT US NOW</h3>
  <svg class="abs contact-icon-pin" width="37" height="42" viewBox="0 0 37 42" aria-hidden="true">
    <polygon points="18.5,0 37,10.5 37,31.5 18.5,42 0,31.5 0,10.5" fill="var(--sky)"/>
    <path d="M18.5 10a6.5 6.5 0 0 0-6.5 6.5c0 5 6.5 12 6.5 12s6.5-7 6.5-12a6.5 6.5 0 0 0-6.5-6.5Zm0 9a2.5 2.5 0 1 1 0-5 2.5 2.5 0 0 1 0 5Z" fill="var(--paper)"/>
  </svg>
  <p class="abs contact-text contact-address">123, Main Road,<br>New York, USA 4567</p>
  <svg class="abs contact-icon-mail" width="38" height="42" viewBox="0 0 38 42" aria-hidden="true">
    <polygon points="19,0 38,10.5 38,31.5 19,42 0,31.5 0,10.5" fill="var(--sky)"/>
    <rect x="10" y="14" width="18" height="13" rx="1.5" fill="var(--paper)"/>
    <path d="M10.5 15l8.5 6.5 8.5-6.5" fill="none" stroke="var(--sky)" stroke-width="1.6"/>
  </svg>
  <p class="abs contact-text contact-web">free@companymail.com<br>www.companyweb.com</p>

</main>
</body>
</html>
```